Rack Card for Portuguese Walking Food Tour

I would like a vertical rack card measuring 99x210mm. Here is the information I would like to include. It does not need to be in this format. We are located in Setubal, Portugal.
Please use the attached Teal Heron Logo.
Setúbal: Tradition and Today
Experience the culinary delights of Setúbal, Portugal with a walking food tour around our waterfront village. Discover the Mercado da Gaivota Branca, voted one of the world’s best markets by Metro Ledger, and indulge in local wines and dishes. Prepare for a calm stroll on flat streets. No hills to climb on this tour.
Duration: 4 hours
www.brinebasketwalks.com
+351 265 000 487

```html
<!DOCTYPE html>
<html lang="en">
<head>
<meta charset="utf-8">
<title>Brine Basket Walks – Rack Card</title>
<link rel="stylesheet" href="https://fonts.googleapis.com/css2?family=Archivo:wght@800&family=Open+Sans:wght@400;600;700&display=swap">
<style>
  :root {
    --orange: #f26522;
    --orange-deep: #e2561a;
    --charcoal: #555657;
    --paper: #eeeeee;
    --side-grey: #d6d6d6;
    --white: #ffffff;
    --fish-red: #d9543f;
    --fish-pink: #f0a08a;
  }
  * { margin: 0; padding: 0; box-sizing: border-box; }
  html, body { width: 1200px; height: 2544px; overflow: hidden; }
  body {
    background: var(--paper);
    font-family: "Open Sans", Arial, sans-serif;
    position: relative;
  }
  .brand {
    position: absolute;
    left: 230px; top: 70px;
    width: 740px; height: 240px;
    background: var(--white);
    border: 6px solid #e4e4e4;
    border-radius: 34px;
    display: flex; align-items: center; justify-content: center; gap: 40px;
  }
  .brand-dot {
    width: 150px; height: 150px; border-radius: 50%;
    background: var(--orange);
    flex: none;
  }
  .brand-name {
    font-family: "Open Sans", Arial, sans-serif;
    font-weight: 700;
    font-size: 76px;
    line-height: 1;
    color: var(--charcoal);
  }
  .title-band {
    position: absolute;
    left: 0; top: 420px; width: 1200px; height: 132px;
    background: var(--charcoal);
    color: var(--white);
    font-family: "Archivo", "Arial Black", sans-serif;
    font-weight: 800;
    font-size: 84px;
    letter-spacing: 1px;
    display: flex; align-items: center; justify-content: center;
  }
  .side-bar {
    position: absolute; top: 760px; width: 60px; height: 1500px;
    background: var(--side-grey);
  }
  .side-bar.left { left: 0; }
  .side-bar.right { right: 0; }
  .market-photo {
    position: absolute;
    left: 72px; top: 568px; width: 1056px; height: 1692px;
    border-radius: 40px;
    background: linear-gradient(160deg, var(--fish-pink) 0%, var(--fish-red) 45%, #b8412f 75%, #8a8d90 100%);
  }
  .story-panel {
    position: absolute;
    left: 88px; top: 1128px; width: 1024px; height: 1104px;
    background: var(--orange);
    border-radius: 36px;
    padding: 36px 44px;
    color: var(--white);
    font-size: 51px;
    line-height: 62px;
    text-align: center;
  }
  .story-panel hr {
    border: none;
    border-top: 4px solid rgba(255,255,255,0.75);
    margin: 26px 0 34px;
  }
  .duration-band {
    position: absolute;
    left: 0; top: 2290px; width: 1200px; height: 132px;
    background: var(--orange);
    color: var(--white);
    font-family: "Archivo", "Arial Black", sans-serif;
    font-weight: 800;
    font-size: 88px;
    display: flex; align-items: center; justify-content: center;
  }
  .contact-band {
    position: absolute;
    left: 0; top: 2422px; width: 1200px; height: 122px;
    background: var(--charcoal);
    color: var(--white);
    font-weight: 700;
    font-size: 50px;
    line-height: 56px;
    text-align: center;
    padding-top: 6px;
  }
</style>
</head>
<body>
  <div class="brand">
    <div class="brand-dot"></div>
    <div class="brand-name">Brine Basket Walks</div>
  </div>

  <div class="title-band">TRADITION AND TODAY</div>

  <div class="side-bar left"></div>
  <div class="side-bar right"></div>

  <div class="market-photo" role="img" aria-label="Photo of fresh red mullet piled on ice at the fish market"></div>

  <div class="story-panel">
    <p>Experience the culinary delights of Setúbal, Portugal with a walking food tour around our waterfront village.</p>
    <hr>
    <p>Discover the Mercado da Gaivota Branca, voted one of the world’s best markets by Metro Ledger, and indulge in local wines and dishes. Prepare for a calm stroll on flat streets. No hills to climb on this tour.</p>
  </div>

  <div class="duration-band">DURATION: 4 HOURS</div>

  <div class="contact-band">
    <div class="contact-web">www.brinebasketwalks.com</div>
    <div class="contact-phone">+351 265 000 487</div>
  </div>
</body>
</html>
```